Marn-ridge Tide Harbor Custom Brokers Limited

Name: Dorvella Hastings
Title: Customs Broker
Address: Shop 9 Birchfield Commercial Complex
207-209 Harlow Road
Kingston 8
Telephone: (876)
Email: tideharborport@quillmail.example

```html
<!DOCTYPE html>
<html lang="en">
<head>
<meta charset="utf-8">
<title>Marn-ridge Tide Harbor Custom Brokers Limited – Business Card</title>
<link rel="stylesheet" href="https://fonts.googleapis.com/css2?family=Roboto:ital,wght@0,400;0,700;1,400;1,700&display=swap">
<style>
  :root {
    --navy: #142c57;
    --gold: #e8a424;
    --white: #ffffff;
    --ink: #3c3f45;
    --rule: #1d3566;
    --backdrop: #2a2a2c;
  }
  * { box-sizing: border-box; margin: 0; padding: 0; }
  html, body {
    width: 1200px; height: 900px; overflow: hidden;
    background: var(--backdrop);
    font-family: "Roboto", Arial, sans-serif;
  }
  .canvas {
    width: 1200px; height: 900px;
    display: flex; flex-direction: column;
    align-items: center; justify-content: center; gap: 44px;
  }
  .card {
    width: 660px; height: 378px;
    position: relative;
    box-shadow: 0 10px 30px rgba(0,0,0,.45);
  }
  .card--front { background: var(--white); }
  .card--back {
    background: var(--navy);
    display: flex; align-items: center; justify-content: center;
  }

  .brand {
    display: flex; align-items: center; gap: 14px;
    font-weight: 700; text-transform: uppercase;
  }
  .brand__dot { width: 18px; height: 18px; border-radius: 50%; background: var(--gold); flex: none; }
  .brand__name { line-height: 1.2; letter-spacing: .04em; }

  .card--front .brand { position: absolute; left: 44px; top: 46px; color: var(--navy); }
  .card--front .brand__name { font-size: 20px; max-width: 330px; }

  .card--back .brand { color: var(--white); }
  .card--back .brand__dot { width: 26px; height: 26px; }
  .card--back .brand__name { font-size: 30px; max-width: 470px; }

  .contact {
    position: absolute; left: 44px; top: 170px;
    list-style: none; font-size: 17px; color: var(--ink);
  }
  .contact li { display: flex; align-items: center; gap: 10px; margin-bottom: 8px; }
  .contact svg { width: 16px; height: 16px; flex: none; }

  .holder {
    position: absolute; right: 44px; top: 196px; text-align: right;
  }
  .holder__name { font-size: 26px; font-weight: 700; font-style: italic; color: var(--navy); }
  .holder__title { font-size: 18px; font-style: italic; color: var(--ink); margin-top: 2px; }

  .divider {
    position: absolute; left: 44px; right: 44px; top: 266px;
    height: 1.5px; background: var(--rule);
  }

  .address {
    position: absolute; right: 44px; top: 286px;
    font-style: italic; font-size: 17px; color: var(--ink);
    text-align: right; line-height: 1.45;
  }
</style>
</head>
<body>
<main class="canvas">
  <section class="card card--front" aria-label="Business card front">
    <div class="brand">
      <span class="brand__dot"></span>
      <span class="brand__name">Marn-ridge Tide Harbor Custom Brokers Limited</span>
    </div>

    <ul class="contact">
      <li>
        <svg viewBox="0 0 16 16" aria-hidden="true"><path fill="#e8a424" d="M3.5 1.5l2.3 2.6-1.3 1.6c.8 1.8 2.1 3.2 3.9 4l1.6-1.3 2.6 2.3-1.3 2.3C6.7 13.3 2.7 9.3 1.2 2.8z"/></svg>
        (876) 555 0142
      </li>
      <li>
        <svg viewBox="0 0 16 16" aria-hidden="true"><rect x="1" y="3" width="14" height="10" fill="#e8a424"/><path d="M1 3l7 6 7-6" fill="none" stroke="#fff" stroke-width="1.3"/></svg>
        tideharborport@quillmail.example
      </li>
    </ul>

    <div class="holder">
      <p class="holder__name">Dorvella Hastings</p>
      <p class="holder__title">Customs Broker</p>
    </div>

    <div class="divider"></div>

    <address class="address">
      Shop 9 Birchfield Commercial Complex<br>
      207-209 Harlow Road, Kingston 8
    </address>
  </section>

  <section class="card card--back" aria-label="Business card back">
    <div class="brand">
      <span class="brand__dot"></span>
      <span class="brand__name">Marn-ridge Tide Harbor Custom Brokers Limited</span>
    </div>
  </section>
</main>
</body>
</html>
```